Redesign of business card for Birchline Mechanical

We are looking for a new design for our business cards for Birchline Mechanical. We are a plumbing & HVAC construction company, operating on the West Coast of Canada and USA. Logo attached.
Industry/Entity Type
Construction - Plumbing & HVAC
Contact Information for Business Card
Name, address, phone numbers, email, website address
Look and feel
Each slider illustrates characteristics of the customer's brand and the style your logo design should communicate.

```html
<!DOCTYPE html>
<html lang="en">
<head>
<meta charset="utf-8">
<title>Birchline Mechanical – Business Card</title>
<link rel="stylesheet" href="https://fonts.googleapis.com/css2?family=Montserrat:wght@400;500;600&display=swap">
<style>
  :root {
    --backdrop: #8cadd6;
    --card-light: #fbfbfb;
    --marble-grey: #ebe9e8;
    --navy-deep: #0a1630;
    --navy-mid: #0d2c4b;
    --ink: #2a2a2a;
    --ink-soft: #4a4a4a;
    --icon-navy: #1d2f5c;
    --white: #ffffff;
    --rule: #5a5a5a;
  }
  * { margin: 0; padding: 0; box-sizing: border-box; }
  html, body {
    width: 1065px; height: 1200px; overflow: hidden;
    background: var(--backdrop);
    font-family: "Montserrat", Arial, sans-serif;
  }
  .canvas { position: relative; width: 1065px; height: 1200px; }
  .card {
    position: absolute; left: 117px; width: 832px; height: 475px;
    overflow: hidden;
    box-shadow: 0 12px 30px rgba(40, 70, 120, 0.35);
  }
  .card--front { top: 113px; }
  .card--back { top: 612px; }
  .card__surface { position: absolute; inset: 0; }
  .card--front .card__surface {
    background:
      radial-gradient(ellipse at 30% 25%, var(--marble-grey) 0%, transparent 45%),
      radial-gradient(ellipse at 75% 80%, var(--marble-grey) 0%, transparent 40%),
      var(--card-light);
  }
  .card--back .card__surface {
    background:
      radial-gradient(ellipse at 45% 55%, var(--navy-mid) 0%, transparent 60%),
      linear-gradient(135deg, var(--navy-mid) 0%, var(--navy-deep) 100%);
  }

  .brand {
    position: absolute; display: flex; align-items: center; gap: 12px;
    font-weight: 600; line-height: 1.1;
  }
  .brand__mark { width: 16px; height: 16px; flex: none; }
  .brand__name { font-size: 27px; letter-spacing: 0.01em; }
  .card--front .brand { left: 62px; top: 205px; color: var(--ink); }
  .card--front .brand__mark { background: var(--ink); }
  .card--back .brand { left: 270px; top: 205px; color: var(--white); }
  .card--back .brand__mark { background: var(--white); }

  .divider {
    position: absolute; left: 378px; top: 108px;
    width: 1px; height: 256px; background: var(--rule);
  }
  .person { position: absolute; left: 428px; top: 108px; }
  .person__name { font-size: 31px; font-weight: 600; color: var(--ink); letter-spacing: -0.01em; }
  .person__title { font-size: 21px; font-weight: 400; color: var(--ink-soft); margin-top: 2px; }

  .contact { position: absolute; left: 428px; top: 224px; list-style: none; }
  .contact__item {
    display: flex; align-items: flex-start; gap: 18px;
    font-size: 18px; color: var(--ink-soft); line-height: 23px;
    margin-bottom: 23px;
  }
  .contact__icon { width: 15px; height: 15px; margin-top: 3px; flex: none; fill: var(--icon-navy); }

  .website {
    position: absolute; left: 0; right: 0; top: 396px;
    text-align: center; color: var(--white);
    font-size: 25px; font-weight: 500; letter-spacing: 0.3em;
  }
</style>
</head>
<body>
<div class="canvas">
  <section class="card card--front">
    <div class="card__surface" role="img" aria-label="Soft white and light grey marbled paper texture"></div>
    <div class="brand"><span class="brand__mark"></span><span class="brand__name">Birchline<br>Mechanical</span></div>
    <div class="divider"></div>
    <div class="person">
      <h1 class="person__name">Daniel Reyes</h1>
      <p class="person__title">CEO | President</p>
    </div>
    <ul class="contact">
      <li class="contact__item">
        <svg class="contact__icon" viewBox="0 0 24 24" aria-hidden="true"><path d="M6.6 10.8c1.4 2.8 3.8 5.1 6.6 6.6l2.2-2.2c.3-.3.7-.4 1-.2 1.1.4 2.3.6 3.6.6.6 0 1 .4 1 1V20c0 .6-.4 1-1 1C10.6 21 3 13.4 3 4c0-.6.4-1 1-1h3.5c.6 0 1 .4 1 1 0 1.3.2 2.5.6 3.6.1.3 0 .7-.2 1L6.6 10.8z"/></svg>
        <span>1 866 555 0147</span>
      </li>
      <li class="contact__item">
        <svg class="contact__icon" viewBox="0 0 24 24" aria-hidden="true"><path d="M2 5h20v2l-10 6L2 7z M2 9l10 6 10-6v10H2z"/></svg>
        <span>info@birchlinemech.com</span>
      </li>
      <li class="contact__item">
        <svg class="contact__icon" viewBox="0 0 24 24" aria-hidden="true"><path d="M12 2a7 7 0 0 0-7 7c0 5 7 13 7 13s7-8 7-13a7 7 0 0 0-7-7zm0 9.5A2.5 2.5 0 1 1 12 6.5a2.5 2.5 0 0 1 0 5z"/></svg>
        <span>4120 Harbor Crest Way,<br>Suite 200, Tustin, CA 92780</span>
      </li>
    </ul>
  </section>

  <section class="card card--back">
    <div class="card__surface" role="img" aria-label="Deep navy and blue marbled ink texture"></div>
    <div class="brand"><span class="brand__mark"></span><span class="brand__name">Birchline<br>Mechanical</span></div>
    <p class="website">www.birchlinemech.com</p>
  </section>
</div>
</body>
</html>
```